Functional Beverage- Flavoured Vitamin Water

Hi,

We need a product label design for a new flavoured vitamin water in London: "Lumo Brisk" .

Lumo Brisk is a refreshing vitamin infusion ready to drink beverage. It is a naturally sweetened (low sugar NOT no sugar, but free from artificial sweetners), with natural colours and flavours - with added vitamins and supplements, including natural botanicals. We want to clearly label this to be a health drink and highlight the benefits. It is a STILL drink and either CLEAR or TINTED RED depending on the flavour.

We have used leading research from the nutritional industry to create functional blends in a light refreshing water that is not sugar laden or artificially flavoured. WE TASTE GREAT!

These are the 4 flavours however for the purposes of the brief I am happy for the designers to focus on either

1. CRANBERRY RASPERRY - rose red - REDOX (contains antioxidants and help immunity)
2. COCONUT PINEAPPLE - clear - BEAUTY (helps maintain hair, skin and nails)

I want the product label to be fresh and stand out as this will be facing competition from established brands (Trevanne / K-Drink).

Labels will be printed on self-adhesive plastic and be applied to a 500 ml PET clear plastic bottle. The label itself would be no more than 190mm wide by 80mm tall and will be a rectangle (to give you an idea of scale when the consumer looks at the label).

I want something as striking, pure and playful as these two brands have on their waters (but not as minimal...)

1. http://thewanderingowl.example/?p=48113
2. http://www.pelmorstudio.example/energy/arch/007215.php
3. Existing bottle is here: https://files.example/QmXpWs83

We will be relying on social media for marketing and PR so fthe design needs to transfer to that type of media well.

Thanks and good luck
Updates

Hi all,

Just a note to the invited designers - hoping some more of you can jump into the project over the weekend if you have not already submitted designs.

Thanks and regards,

Tom

Reason: Extending so we can get some more designs submitted. Thanks.

Hi,

I have increased the budget to allow for a $100 2nd prize, as we are seeing some strong designs in the closing stages.

Regards,
Tom

Reason: Collating final feedback on submissions.

Target Market(s)

18-35 yeare old professionals who consume vitamin supplements and want a ready to drink flavoured water that's different to the standard offering.

It is unisex but feel the brand may appeal more to women initially. But I dont want to disenfranchise men.

Industry/Entity Type

Marketing

Requirements
Must have
• Health benefit claims
Flavour names
Mention the natural fruit sugars and stevia
Nice to have
• Mention how it's "Low Cal not No Cal"

I like the idea of a clear or semi clear label that uses the back of the label on the opposite side like the OKRA water bottle in the attached file. This makes it looks so much more 3d than a "front" label... not a mandatory requirement - just an idea to think of.

```html
<!DOCTYPE html>
<html lang="en">
<head>
<meta charset="utf-8">
<title>Lumo Brisk – Coconut Pineapple Label</title>
<link rel="stylesheet" href="https://fonts.googleapis.com/css2?family=Comfortaa:wght@300;400&display=swap">
<style>
  :root {
    --label-bg: #ffffff;
    --ink-grey: #4a4a4c;
    --ink-blue: #2a9fd8;
    --fruit-yellow: #f3e36a;
    --splash-blue: #3a5a8c;
  }
  html, body {
    margin: 0;
    padding: 0;
    overflow: hidden;
    background: var(--label-bg);
  }
  .label {
    position: relative;
    width: 1200px;
    height: 1000px;
    overflow: hidden;
    background: var(--label-bg);
    font-family: "Comfortaa", sans-serif;
    font-weight: 300;
  }
  .brand-name {
    position: absolute;
    left: 155px;
    top: 915px;
    margin: 0;
    transform: rotate(-90deg);
    transform-origin: left top;
    white-space: nowrap;
    font-size: 138px;
    line-height: 150px;
    font-weight: 300;
    color: var(--ink-grey);
    letter-spacing: 1px;
  }
  .brand-descriptor {
    position: absolute;
    left: 326px;
    top: 666px;
    margin: 0;
    transform: rotate(-90deg);
    transform-origin: left top;
    white-space: nowrap;
    font-size: 41px;
    line-height: 46px;
    color: var(--ink-blue);
  }
  .flavour-visual {
    position: absolute;
    left: 375px;
    top: 150px;
    width: 660px;
    height: 600px;
  }
  .benefit-line {
    position: absolute;
    left: 318px;
    top: 803px;
    margin: 0;
    white-space: nowrap;
    font-size: 43px;
    line-height: 60px;
    color: var(--ink-grey);
  }
  .volume {
    position: absolute;
    right: 198px;
    top: 862px;
    margin: 0;
    font-size: 46px;
    line-height: 60px;
    color: var(--ink-blue);
  }
</style>
</head>
<body>
  <main class="label">
    <h1 class="brand-name">Lumo Brisk</h1>
    <p class="brand-descriptor">natural | vitamin | beverage</p>

    <svg class="flavour-visual" viewBox="0 0 660 600" role="img" aria-label="Photo of a halved pineapple with slices, an open coconut and a splash of water">
      <defs>
        <radialGradient id="fruit-glow" cx="0.4" cy="0.6" r="0.6">
          <stop offset="0" stop-color="#f3e36a"/>
          <stop offset="0.6" stop-color="#e9d98a" stop-opacity="0.8"/>
          <stop offset="1" stop-color="#ffffff" stop-opacity="0"/>
        </radialGradient>
        <radialGradient id="splash-glow" cx="0.75" cy="0.25" r="0.45">
          <stop offset="0" stop-color="#3a5a8c" stop-opacity="0.45"/>
          <stop offset="1" stop-color="#ffffff" stop-opacity="0"/>
        </radialGradient>
      </defs>
      <rect width="660" height="600" fill="url(#splash-glow)"/>
      <rect width="660" height="600" fill="url(#fruit-glow)"/>
    </svg>

    <p class="benefit-line">your hair,skin &amp; nails will love it</p>
    <p class="volume">500 ML</p>
  </main>
</body>
</html>
```